New Business Card for Software Company

We are looking at rebranding a 10 year old company that specializes in PDF and DWF solutions for Architects and Engineers. We will attach the new company logo that we are going with so you can work with that and complimentary colors.
The sample information we would like on the business card is:
Gerald Pembrook
Vice President
4173 W. Tillman Avenue. STE 306
PMB#417
Mesa, AZ 85316
866-392-7154 US Toll Free
123-581-3064 Cell
gpembrook@vextrolan.com
The old tag line that we had on the business cars was.
Providing Industrial Strength PDF and DWF Solutions to the Global CAD Marketplace.
If you have an idea for a better tag line we are open to that also.
Updates
We would like to thank all of the Designers for their wonderful work. We apologize that we will not have the time to provide feedback to everyone. There is just so many innovative and professional designs that you have all created making our decision even harder.
Target Market(s)
Architects and Engineers
Industry/Entity Type
Business
Look and feel
Each slider illustrates characteristics of the customer's brand and the style your logo design should communicate.

```html
<!DOCTYPE html>
<html lang="en">
<head>
<meta charset="utf-8">
<title>Vextrolan Business Card</title>
<link rel="stylesheet" href="https://fonts.googleapis.com/css2?family=Open+Sans:wght@400;600;800&display=swap">
<style>
  :root {
    --bg: #ece8e3;
    --card: #ffffff;
    --orange: #e8571c;
    --grey: #5d5d5f;
    --text: #3f3f41;
    --faint: #fbeee6;
  }
  * { margin: 0; padding: 0; box-sizing: border-box; }
  html, body {
    width: 1200px; height: 720px; overflow: hidden;
    background: var(--bg);
    font-family: "Open Sans", Arial, sans-serif;
  }
  .stage {
    position: relative; width: 1200px; height: 720px;
    display: flex; justify-content: center; align-items: center; gap: 40px;
  }
  .card {
    position: relative; width: 540px; height: 309px;
    background: var(--card); overflow: hidden;
    box-shadow: 0 3px 10px rgba(0,0,0,.12);
  }
  .faint-disc {
    position: absolute; border-radius: 50%; background: var(--faint);
  }
  .card-contact .faint-disc { width: 230px; height: 230px; right: 10px; top: -40px; }
  .card-brand .faint-disc { width: 230px; height: 230px; left: -60px; top: 10px; }

  .brand-mark { display: flex; align-items: center; gap: 10px; }
  .brand-dot { width: 40px; height: 40px; border-radius: 50%; background: var(--orange); flex: none; }
  .brand-name { font-weight: 800; color: var(--orange); letter-spacing: -1px; line-height: 1; }

  .card-contact .brand-mark { position: absolute; left: 34px; top: 34px; }
  .card-contact .brand-name { font-size: 40px; }

  .person { position: absolute; left: 34px; top: 112px; }
  .person-name { color: var(--orange); font-weight: 600; font-size: 15px; }
  .person-title { color: var(--grey); font-size: 12px; font-weight: 400; }

  .contacts { position: absolute; left: 34px; top: 146px; list-style: none; }
  .contacts li {
    display: flex; align-items: center; gap: 8px;
    font-size: 12.5px; color: var(--text); line-height: 22px;
  }
  .contacts svg { width: 12px; height: 12px; fill: var(--orange); flex: none; }

  .address {
    position: absolute; left: 34px; top: 226px;
    font-size: 12.5px; color: var(--text); line-height: 20px; font-style: normal;
  }

  .card-brand .brand-mark { position: absolute; right: 36px; top: 92px; }
  .card-brand .brand-dot { width: 56px; height: 56px; }
  .card-brand .brand-name { font-size: 66px; }
  .tagline {
    position: absolute; right: 36px; top: 188px; width: 400px;
    text-align: right; color: var(--grey); font-size: 15.5px; line-height: 21px;
  }
</style>
</head>
<body>
<main class="stage">
  <section class="card card-contact">
    <div class="faint-disc"></div>
    <div class="brand-mark">
      <span class="brand-dot"></span>
      <span class="brand-name">Vextrolan</span>
    </div>
    <p class="person"><span class="person-name">Gerald Pembrook,</span> <span class="person-title">Vice President</span></p>
    <ul class="contacts">
      <li>
        <svg viewBox="0 0 24 24"><path d="M6.6 10.8a15 15 0 0 0 6.6 6.6l2.2-2.2a1 1 0 0 1 1-.25 11.4 11.4 0 0 0 3.6.57 1 1 0 0 1 1 1V20a1 1 0 0 1-1 1A17 17 0 0 1 3 4a1 1 0 0 1 1-1h3.5a1 1 0 0 1 1 1c0 1.25.2 2.45.57 3.57a1 1 0 0 1-.25 1z"/></svg>
        866-392-7154US(TF)
      </li>
      <li>
        <svg viewBox="0 0 24 24"><path d="M7 1h10a2 2 0 0 1 2 2v18a2 2 0 0 1-2 2H7a2 2 0 0 1-2-2V3a2 2 0 0 1 2-2zm0 3v14h10V4zm5 15.5a1.2 1.2 0 1 0 0 2.4 1.2 1.2 0 0 0 0-2.4z"/></svg>
        123-581-3064
      </li>
      <li>
        <svg viewBox="0 0 24 24"><path d="M2 5h20v14H2zm2 2v.4l8 5.2 8-5.2V7zm0 2.8V17h16V9.8l-8 5.2z"/></svg>
        gpembrook@vextrolan.com
      </li>
    </ul>
    <address class="address">
      4173 W. Tillman Avenue. STE 306<br>
      PMB#417, Mesa, AZ 85316
    </address>
  </section>

  <section class="card card-brand">
    <div class="faint-disc"></div>
    <div class="brand-mark">
      <span class="brand-dot"></span>
      <span class="brand-name">Vextrolan</span>
    </div>
    <p class="tagline">Providing Industrial Strength PDF and<br>DWF Solutions to the Global CAD Marketplace</p>
  </section>
</main>
</body>
</html>
```